Shotcrete Contractor Needs Business Cards Designed

We're a Shotcrete construction company based out of Southern California who opened another office in Northern California and needs new cards. The cards need to have our logo,name,title,license #,contact info, and website. Both office locations need to be on the card as well. We are looking for a professional clean design that will work well in the construction industry. PLEASE VISIT THE WEBSITE to get a feel about the company. www.harborlineshotcrete.example

Industry/Entity Type

Construction

```html
<!DOCTYPE html>
<html lang="en">
<head>
<meta charset="utf-8">
<title>Harborline Shotcrete Business Card</title>
<link href="https://fonts.googleapis.com/css2?family=Open+Sans:wght@400;600;700&display=swap" rel="stylesheet">
<style>
  :root {
    --backdrop: #e4e5e8;
    --paper: #ffffff;
    --navy: #1c2a7a;
    --red: #c8202a;
    --grey: #6b6b6b;
    --ink: #4a4a4a;
  }
  * { box-sizing: border-box; margin: 0; padding: 0; }
  html, body {
    width: 1200px; height: 900px; overflow: hidden;
    background: var(--backdrop);
    font-family: "Open Sans", Arial, sans-serif;
  }
  .canvas { position: relative; width: 1200px; height: 900px; }
  .card {
    position: absolute; left: 250px;
    width: 700px; height: 400px;
    background: var(--paper);
    box-shadow: 0 6px 18px rgba(0,0,0,0.18);
    overflow: hidden;
  }
  .card--back { top: 30px; }
  .card--front { top: 470px; }

  /* Back face */
  .brand-mark {
    position: absolute; left: 0; right: 0; top: 120px; height: 80px;
    display: flex; align-items: center; justify-content: center; gap: 18px;
  }
  .brand-square { width: 40px; height: 40px; background: var(--red); flex: none; }
  .brand-name {
    font-size: 36px; font-weight: 700; color: var(--navy);
    letter-spacing: 1px; text-transform: uppercase; white-space: nowrap;
  }
  .back-details {
    position: absolute; right: 44px; bottom: 36px; text-align: right;
    font-size: 13px; line-height: 19px; color: var(--grey);
  }
  .back-details .office-label {
    font-weight: 700; color: var(--navy); text-transform: uppercase;
  }
  .license { margin-top: 8px; color: var(--ink); }
  .back-details address { font-style: normal; }

  /* Front face */
  .front-logo {
    position: absolute; left: 46px; top: 78px;
    display: flex; align-items: center; gap: 12px;
  }
  .front-logo .brand-square { width: 26px; height: 26px; }
  .front-logo .brand-name { font-size: 22px; letter-spacing: 0.5px; }

  .person { position: absolute; right: 44px; top: 38px; text-align: right; }
  .person-name { font-size: 20px; color: var(--navy); }
  .person-title { font-size: 14px; color: var(--grey); margin-top: 2px; }

  .contact {
    position: absolute; right: 44px; top: 160px; text-align: right;
    font-size: 15px; line-height: 21px; color: var(--ink);
  }

  .office {
    position: absolute; left: 46px; top: 250px; font-style: normal;
    font-size: 16px; line-height: 21px; color: var(--grey);
  }
  .office-company { font-size: 15px; font-weight: 700; color: var(--navy); text-transform: uppercase; }

  .band { position: absolute; left: 0; right: 0; bottom: 0; height: 46px; background: var(--navy); }
</style>
</head>
<body>
<main class="canvas">

  <section class="card card--back" aria-label="Card back">
    <div class="brand-mark">
      <span class="brand-square"></span>
      <span class="brand-name">Harborline Shotcrete</span>
    </div>
    <div class="back-details">
      <address>
        <p class="office-label">Northern California Office</p>
        <p>1275 Redwood Parkway</p>
        <p>Suite 204, Santa Rosa, CA 95403</p>
      </address>
      <p class="license">Lic. # 900072</p>
    </div>
  </section>

  <section class="card card--front" aria-label="Card front">
    <div class="front-logo">
      <span class="brand-square"></span>
      <span class="brand-name">Harborline Shotcrete</span>
    </div>

    <div class="person">
      <p class="person-name">Daniel Marwick</p>
      <p class="person-title">managing director</p>
    </div>

    <div class="contact">
      <p>T - 800-555-0148</p>
      <p>F - 661-555-0193</p>
      <p>dmarwick@harborlineshotcrete.example</p>
      <p>www.harborlineshotcrete.example</p>
    </div>

    <address class="office">
      <p class="office-company">Harborline Shotcrete, Inc.</p>
      <p>4410 Tidewater Road</p>
      <p>Suite 118, Valley Glen</p>
      <p>CA 91401</p>
    </address>

    <div class="band"></div>
  </section>

</main>
</body>
</html>
```